Saffron Lantern Court Business Card

I am looking for a business card desgined for my restaurant. It is an Indian restaurant, we are looking for something thats modern, yet traditional with the indian culture, we are looking for colors that match our logo. The logo is a design of the building with the name of the restaurant. for more information on the restaurant go to www.saffronlanterncourt.example

Industry/Entity Type

Indian Restaurant

Contact Information for Business Card

we are looking for somthing thats modern, yet traditional with the indian culture, we are looking for colors that match our logo. The logo is a design of the building with the name of the restaurant. for more information on the restaurant go to www.saffronlanterncourt.example

Requirements
Must have
• The logo that is attached,
• Name: Harvinder Oberoi,
• address of the restaurant: 7328 West Larkspur Rd, Phoenix, Arizona, 85213
• Phone: (602) 555-0147
• Fax: (602) 555-0193
• Restaurant Catering Banquet
• Website: www.SaffronLanternCourt.example
Nice to have
• wanted to get something that goes with the theme of the restaurant, which is traditional but also keep a very professional and modern touch

```html
<!DOCTYPE html>
<html lang="en">
<head>
<meta charset="utf-8">
<title>Saffron Lantern Court – Business Card</title>
<link rel="stylesheet" href="https://fonts.googleapis.com/css2?family=Cinzel:wght@700&family=Bebas+Neue&family=Archivo+Black&display=swap">
<style>
  :root {
    --bg: #cbcbcb;
    --paper: #ffffff;
    --brand-red: #a3201f;
    --deep-red: #9b1c1c;
    --green: #2ea548;
    --orange: #f07022;
    --orange-light: #f7a045;
    --icon-dark: #333333;
    --white: #ffffff;
  }
  * { margin: 0; padding: 0; box-sizing: border-box; }
  html, body { width: 1200px; height: 1200px; overflow: hidden; background: var(--bg); }
  .canvas { position: relative; width: 1200px; height: 1200px; }

  .card { position: absolute; left: 212px; width: 777px; height: 431px; overflow: hidden; }
  .card--front { top: 113px; background: var(--paper); }
  .card--back { top: 655px; }

  .band { position: absolute; top: 173px; height: 86px;
          background: linear-gradient(90deg, var(--deep-red), var(--orange) 45%, var(--green)); }
  .band--left { left: 0; width: 64px; border-radius: 0 40px 40px 0; }
  .band--right { left: 460px; width: 317px; border-radius: 40px 0 0 40px; }

  .brand-name {
    position: absolute; left: 148px; top: 160px; width: 240px;
    font-family: "Cinzel", serif; font-weight: 700; font-size: 44px; line-height: 50px;
    color: var(--brand-red); text-align: center; letter-spacing: 1px;
  }

  .back-art { position: absolute; inset: 0; }
  .holder-name {
    position: absolute; left: 86px; top: 86px;
    font-family: "Bebas Neue", sans-serif; font-size: 50px; line-height: 44px;
    color: var(--white); letter-spacing: 0.5px;
  }
  .contact {
    position: absolute; font-family: "Archivo Black", sans-serif; font-size: 12px;
    line-height: 15px; color: var(--white); letter-spacing: 0.4px;
  }
  .contact--phone { left: 313px; top: 323px; }
  .contact--fax { left: 311px; top: 382px; }
  .contact--address { left: 541px; top: 315px; }
  .contact--web { left: 539px; top: 382px; font-size: 11px; }
</style>
</head>
<body>
<main class="canvas">

  <section class="card card--front" aria-label="Card front">
    <div class="band band--left" role="img" aria-label="Decorative chevron pattern band in red, green and orange"></div>
    <div class="band band--right" role="img" aria-label="Decorative chevron pattern band in red, green and orange"></div>
    <h1 class="brand-name">Saffron Lantern Court</h1>
  </section>

  <section class="card card--back" aria-label="Card back">
    <svg class="back-art" width="777" height="431" viewBox="0 0 777 431">
      <defs>
        <linearGradient id="patternTone" x1="0" y1="0" x2="1" y2="1">
          <stop offset="0" stop-color="#9b1c1c"/>
          <stop offset="0.5" stop-color="#b8402a"/>
          <stop offset="1" stop-color="#3f8f3e"/>
        </linearGradient>
      </defs>
      <rect width="777" height="431" fill="url(#patternTone)" role="img" aria-label="Decorative ogee diamond pattern in red, green and orange"/>
      <path class="panel-light" d="M248 282 Q252 262 278 262 H777 V282 Z" fill="var(--orange-light)"/>
      <path class="panel-main" d="M104 431 L190 310 Q210 281 252 281 H777 V431 Z" fill="var(--orange)"/>
      <path class="panel-corner" d="M0 332 H80 Q100 332 100 352 V431 H0 Z" fill="var(--orange)"/>

      <g class="icon icon--phone" transform="translate(273 330)">
        <circle r="19" fill="var(--icon-dark)"/>
        <path d="M-8 -9 L-3 -10 L0 -4 L-3 -1 Q0 4 4 6 L7 3 L12 6 L10 11 Q-10 10 -11 -7 Z" fill="var(--white)"/>
      </g>
      <g class="icon icon--fax" transform="translate(273 389)">
        <circle r="19" fill="var(--icon-dark)"/>
        <rect x="-3" y="-11" width="9" height="9" fill="var(--white)"/>
        <rect x="-9" y="-3" width="20" height="12" rx="2" fill="var(--white)"/>
        <rect x="-13" y="-3" width="3" height="13" fill="var(--white)"/>
      </g>
      <g class="icon icon--pin" transform="translate(502 330)">
        <circle r="19" fill="var(--icon-dark)"/>
        <path d="M0 12 Q-9 1 -9 -3 A9 9 0 1 1 9 -3 Q9 1 0 12 Z" fill="var(--white)"/>
        <circle cy="-3" r="3.5" fill="var(--icon-dark)"/>
      </g>
      <g class="icon icon--globe" transform="translate(502 389)">
        <circle r="19" fill="var(--icon-dark)"/>
        <g fill="none" stroke="var(--white)" stroke-width="1.6">
          <circle r="11"/>
          <ellipse rx="5" ry="11"/>
          <line x1="-11" y1="0" x2="11" y2="0"/>
          <line x1="0" y1="-11" x2="0" y2="11"/>
          <path d="M-9 -6 H9 M-9 6 H9"/>
        </g>
      </g>
    </svg>

    <h2 class="holder-name">Harvinder Oberoi</h2>
    <p class="contact contact--phone">(602) 555-0147</p>
    <p class="contact contact--fax">(602) 555-0193</p>
    <p class="contact contact--address">7328 West Larkspur Rd, Phoenix,<br>Arizona, 85213</p>
    <p class="contact contact--web">www.SaffronLanternCourt.example</p>
  </section>

</main>
</body>
</html>
```